Business Cards for a law firm

Business cards for our law firm. Use our silhoette logo and OAK HARBOR - check our website (www.oakharbor-legal.com)

Contact Information for Business Card

our silhouette logo, OAK HARBOR, 800-555-0147, Dorian Kestrup, dorian@oakharbor-legal.com

Requirements
Must have
• our silhouette logo, OAK HARBOR, 800-555-0147, Dorian Kestrup, dorian@oakharbor-legal.com

```html
<!DOCTYPE html>
<html lang="en">
<head>
<meta charset="utf-8">
<title>Oak Harbor — Business Cards</title>
<link rel="stylesheet" href="https://fonts.googleapis.com/css2?family=Montserrat:wght@700&family=Open+Sans:wght@400;700&display=swap">
<style>
  :root {
    --navy: #22346c;
    --navy-deep: #1d2c5e;
    --white: #ffffff;
    --ink: #1a1f2e;
    --backdrop: #3a3a3a;
  }
  * { box-sizing: border-box; margin: 0; padding: 0; }
  html, body { width: 1200px; height: 1200px; overflow: hidden; }
  body {
    background: var(--backdrop);
    position: relative;
    font-family: "Open Sans", Arial, sans-serif;
  }
  .card {
    position: absolute;
    left: 150px;
    width: 900px;
    height: 514px;
    border-radius: 36px;
    overflow: hidden;
  }
  .card--back { top: 60px; background: var(--navy); }
  .card--front { top: 626px; background: var(--white); }

  .brand {
    position: absolute;
    display: flex;
    align-items: center;
    gap: 24px;
  }
  .brand__mark { width: 64px; height: 64px; }
  .brand__name {
    font-family: "Montserrat", Arial, sans-serif;
    font-weight: 700;
    font-size: 70px;
    letter-spacing: 4px;
    line-height: 1;
    white-space: nowrap;
  }
  .card--back .brand { left: 50%; top: 50%; transform: translate(-50%, -50%); }
  .card--back .brand__mark { background: var(--navy-deep); }
  .card--back .brand__name { color: var(--navy-deep); }

  .card--front .brand { left: 60px; top: 90px; }
  .card--front .brand__mark { background: var(--navy); }
  .card--front .brand__name { color: var(--navy); }

  .person {
    position: absolute;
    left: 150px;
    top: 215px;
    text-align: right;
  }
  .person__name {
    font-weight: 700;
    font-size: 40px;
    color: var(--navy);
    line-height: 1.1;
  }
  .person__role {
    font-size: 20px;
    color: var(--ink);
  }
  .divider {
    position: absolute;
    left: 475px;
    top: 200px;
    width: 2px;
    height: 110px;
    background: var(--navy);
  }
  .contacts {
    position: absolute;
    left: 495px;
    top: 200px;
    list-style: none;
  }
  .contacts li {
    display: flex;
    align-items: center;
    gap: 12px;
    font-size: 21px;
    color: var(--ink);
    height: 36px;
  }
  .contacts svg { width: 20px; height: 20px; fill: var(--navy); flex: none; }
  .wave { position: absolute; left: 0; top: 0; width: 900px; height: 514px; }
</style>
</head>
<body>
  <section class="card card--back">
    <div class="brand">
      <span class="brand__mark"></span>
      <span class="brand__name">OAK HARBOR</span>
    </div>
  </section>

  <section class="card card--front">
    <svg class="wave" viewBox="0 0 900 514" aria-hidden="true">
      <path d="M0,514 L0,492 C220,402 440,400 620,382 C760,368 860,302 900,232 L900,514 Z" fill="var(--navy)"/>
      <path d="M250,440 C420,385 600,372 700,355 C800,338 860,280 885,230" fill="none" stroke="var(--navy)" stroke-width="3"/>
    </svg>

    <div class="brand">
      <span class="brand__mark"></span>
      <span class="brand__name">OAK HARBOR</span>
    </div>

    <div class="person">
      <p class="person__name">Dorian Kestrup</p>
      <p class="person__role">Lawyer</p>
    </div>

    <span class="divider"></span>

    <ul class="contacts">
      <li>
        <svg viewBox="0 0 24 24" aria-hidden="true"><path d="M6.6 10.8a15 15 0 0 0 6.6 6.6l2.2-2.2a1 1 0 0 1 1-.25 11.4 11.4 0 0 0 3.6.57 1 1 0 0 1 1 1V20a1 1 0 0 1-1 1A17 17 0 0 1 3 4a1 1 0 0 1 1-1h3.5a1 1 0 0 1 1 1c0 1.25.2 2.45.57 3.57a1 1 0 0 1-.25 1z"/></svg>
        800-555-0147
      </li>
      <li>
        <svg viewBox="0 0 24 24" aria-hidden="true"><path d="M2 5h20v14H2z M2 5l10 8 10-8" /></svg>
        dorian@oakharbor-legal.com
      </li>
      <li>
        <svg viewBox="0 0 24 24" aria-hidden="true"><circle cx="12" cy="12" r="10"/></svg>
        www.oakharbor-legal.com
      </li>
    </ul>
  </section>
</body>
</html>
```